Vornel Technologies business card design

We need a business card designed with our new logo. it would be great if the card could communicate it is a technology based company.

Target Market(s)

system integrators

Industry/Entity Type

technology, IOT

Contact Information for Business Card

Name, designation, Address, telephone number, email address

Requirements
Must have
• logo and company name
Nice to have
• something to do with technology

```html
<!DOCTYPE html>
<html lang="en">
<head>
<meta charset="utf-8">
<title>Vornel Technologies – Business Card</title>
<link href="https://fonts.googleapis.com/css2?family=Exo+2:wght@400;500;700;800&display=swap" rel="stylesheet">
<style>
  :root {
    --backdrop: #bdbdbd;
    --brand-orange: #f5951f;
    --brand-orange-light: #f8a940;
    --ink-dark: #333335;
    --card-white: #ffffff;
    --pattern-grey: #ececec;
  }
  * { box-sizing: border-box; margin: 0; padding: 0; }
  html, body { width: 1200px; height: 900px; overflow: hidden; }
  body {
    background: var(--backdrop);
    font-family: "Exo 2", sans-serif;
    position: relative;
  }
  .card {
    position: absolute;
    width: 520px;
    height: 300px;
    border-radius: 26px;
    overflow: hidden;
    box-shadow: 0 10px 22px rgba(0,0,0,0.28);
  }
  .card--front { left: 50px; top: 300px; background: var(--brand-orange); }
  .card--back  { left: 630px; top: 300px; background: var(--card-white); }

  .card__pattern {
    position: absolute;
    top: 0; right: 0;
    width: 70%;
    height: 75%;
  }
  .card--front .card__pattern {
    background: radial-gradient(ellipse at 70% 30%, var(--brand-orange-light), rgba(245,149,31,0) 70%);
  }
  .card--back .card__pattern {
    background: radial-gradient(ellipse at 75% 25%, var(--pattern-grey), rgba(255,255,255,0) 70%);
  }

  .brand {
    position: absolute;
    display: flex;
    align-items: center;
    gap: 14px;
    font-weight: 800;
    text-transform: uppercase;
    letter-spacing: 2px;
    line-height: 1;
  }
  .brand__square { width: 22px; height: 22px; flex: none; }
  .card--front .brand {
    left: 0; right: 0; top: 128px;
    justify-content: center;
    color: var(--card-white);
    font-size: 34px;
  }
  .card--front .brand__square { background: var(--card-white); }
  .card--back .brand {
    left: 50px; top: 70px;
    color: var(--ink-dark);
    font-size: 32px;
  }
  .card--back .brand__square { background: var(--brand-orange); }

  .person { position: absolute; left: 50px; top: 168px; }
  .person__name {
    font-weight: 700;
    font-size: 22px;
    letter-spacing: 1px;
    color: var(--ink-dark);
    text-transform: uppercase;
  }
  .person__role {
    font-weight: 500;
    font-size: 15px;
    color: var(--brand-orange);
    margin-top: 2px;
  }
  .contact {
    position: absolute; left: 50px; top: 232px;
    list-style: none;
    font-size: 14px;
    color: var(--ink-dark);
  }
  .contact li { display: flex; align-items: center; gap: 8px; line-height: 22px; }
  .contact svg { width: 14px; height: 14px; flex: none; }

  .address {
    position: absolute; right: 40px; top: 170px;
    text-align: right;
    font-size: 13px;
    font-weight: 500;
    color: var(--ink-dark);
    font-style: normal;
    line-height: 18px;
  }
</style>
</head>
<body>

<section class="card card--front" aria-label="Card front">
  <div class="card__pattern" role="img" aria-label="Faint pattern of overlapping tech squares"></div>
  <div class="brand"><span class="brand__square"></span>Vornel Technologies</div>
</section>

<section class="card card--back" aria-label="Card back">
  <div class="card__pattern" role="img" aria-label="Faint pattern of overlapping tech squares"></div>
  <div class="brand"><span class="brand__square"></span>Vornel Technologies</div>

  <div class="person">
    <p class="person__name">Marcus Dellow</p>
    <p class="person__role">Managing Director</p>
  </div>

  <ul class="contact">
    <li>
      <svg viewBox="0 0 24 24" aria-hidden="true"><path fill="var(--brand-orange)" d="M6.6 10.8a15.1 15.1 0 0 0 6.6 6.6l2.2-2.2c.3-.3.7-.4 1-.2 1.1.4 2.3.6 3.6.6.6 0 1 .4 1 1V20c0 .6-.4 1-1 1A17 17 0 0 1 3 4c0-.6.4-1 1-1h3.5c.6 0 1 .4 1 1 0 1.3.2 2.5.6 3.6.1.3 0 .7-.2 1z"/></svg>
      044-987 654 321
    </li>
    <li>
      <svg viewBox="0 0 24 24" aria-hidden="true"><path fill="var(--brand-orange)" d="M2 5h20v14H2zm2 2v.5l8 5 8-5V7l-8 5z"/></svg>
      hello@vornelmail.com
    </li>
  </ul>

  <address class="address">
    87, Harbour Row Street<br>
    30918,Country Name
  </address>
</section>

</body>
</html>
```